A5 Certificate for a running Bluecrest Challenge

I would like a certificate designed called the "Bluecrest 50K Running Challenge"

It is presented to people that have run 50k in Mallorca across 10 runs. So they have to run 10 runs with a minimum distance of 5K per run. This gives a total of 50k.

The certificate will need:

1. Map of Mallorca in the background
2. Picture of a runner
3. Main title at the front to say "Bluecrest 50k Running Challenge"
4. Space to put the runners name on it. "Awarded to:"
5. Space to put the date the certificate is awarded. "Date Awarded:"

The design is then up to you but it needs to look official and professional. It is designed for teenagers so it needs to be "cool" and bold.

Any questions please ask.

Target Market(s)

Teenagers who want something cool and bold.

Font styles to use
Sans Serif

Colors
0556a4
fbee3f
33a6d7

Requirements
Must have
• 1. Map of Mallorca in the background
• 2. Picture of a runner
• 3. Main title at the front to say "Bluecrest 50k Running Challenge"
• 4. Space to put the runners name on it. "Awarded to:"
• 5. Space to put the date the certificate is awarded. "Date Awarded:"
Nice to have
• Mallorca is a sunny holiday location so it would be good to have sea blue colours and the sun in the design. to show the running challenge was done on a holiday island.

```html
<!DOCTYPE html>
<html lang="en">
<head>
<meta charset="utf-8">
<title>Bluecrest 50k Running Challenge Certificate</title>
<link rel="stylesheet" href="https://fonts.googleapis.com/css2?family=Marcellus&family=Bodoni+Moda:wght@500&family=Pinyon+Script&family=PT+Sans&family=PT+Sans+Narrow&display=swap">
<style>
  :root {
    --page-bg: #dcdde1;
    --card-bg: #ffffff;
    --ink-navy: #15154a;
    --ink-soft: #4a4a6a;
    --frame-grey: #6e6e78;
    --rule-lilac: #b9b8cc;
    --map-peach: #f4a77a;
    --wave-blue: #5fb3e6;
    --wave-red: #ef3d22;
    --runner-yellow: #f5d31a;
  }
  html, body {
    margin: 0;
    width: 1200px;
    height: 1200px;
    overflow: hidden;
    background: var(--page-bg);
  }
  .certificate {
    position: absolute;
    left: 124px;
    top: 258px;
    width: 978px;
    height: 690px;
    background: var(--card-bg);
    overflow: hidden;
  }
  .certificate__art {
    position: absolute;
    inset: 0;
  }
  .certificate__text {
    position: absolute;
    margin: 0;
    white-space: nowrap;
    color: var(--ink-navy);
    font-weight: 400;
  }
  .event-name {
    left: 0; right: 0;
    top: 131px;
    text-align: center;
    font-family: "Marcellus", serif;
    font-size: 54px;
    letter-spacing: 8px;
    line-height: 1;
  }
  .event-distance {
    left: 305px;
    top: 177px;
    font-family: "Bodoni Moda", serif;
    font-weight: 500;
    font-size: 232px;
    line-height: 1;
    letter-spacing: -10px;
  }
  .event-subtitle {
    left: 0; right: 0;
    top: 417px;
    text-align: center;
    font-family: "Marcellus", serif;
    font-size: 68px;
    letter-spacing: 2px;
    line-height: 1;
  }
  .awarded-label {
    left: 155px;
    top: 528px;
    font-family: "PT Sans", sans-serif;
    font-size: 20px;
  }
  .awardee-line {
    position: absolute;
    left: 301px;
    top: 548px;
    width: 521px;
    height: 2px;
    background: var(--rule-lilac);
  }
  .awardee-name {
    left: 358px;
    top: 480px;
    font-family: "Pinyon Script", cursive;
    font-size: 60px;
    line-height: 1.1;
  }
  .award-date {
    left: 0; right: 0;
    top: 585px;
    text-align: center;
    font-family: "PT Sans Narrow", sans-serif;
    font-size: 23px;
    color: var(--ink-soft);
  }
  .award-location {
    left: 0; right: 0;
    top: 614px;
    text-align: center;
    font-family: "PT Sans Narrow", sans-serif;
    font-size: 16px;
  }
</style>
</head>
<body>
  <main class="certificate">
    <svg class="certificate__art" width="978" height="690" viewBox="0 0 978 690">
      <defs>
        <linearGradient id="wave-blue-band" x1="0" y1="0" x2="1" y2="0">
          <stop offset="0" stop-color="var(--wave-blue)" stop-opacity="0.75"/>
          <stop offset="0.35" stop-color="var(--wave-blue)" stop-opacity="0.25"/>
          <stop offset="0.6" stop-color="var(--wave-blue)" stop-opacity="0"/>
        </linearGradient>
        <linearGradient id="wave-red-band" x1="0" y1="0" x2="1" y2="0">
          <stop offset="0.4" stop-color="var(--wave-red)" stop-opacity="0"/>
          <stop offset="0.75" stop-color="#f7822c" stop-opacity="0.55"/>
          <stop offset="1" stop-color="var(--wave-red)" stop-opacity="0.9"/>
        </linearGradient>
        <radialGradient id="island-tone" cx="0.5" cy="0.45" r="0.6">
          <stop offset="0" stop-color="var(--map-peach)" stop-opacity="0.8"/>
          <stop offset="1" stop-color="var(--map-peach)" stop-opacity="0.4"/>
        </radialGradient>
        <linearGradient id="runner-tone" x1="0" y1="0" x2="1" y2="1">
          <stop offset="0" stop-color="var(--runner-yellow)" stop-opacity="0.55"/>
          <stop offset="0.5" stop-color="#f59a8a" stop-opacity="0.45"/>
          <stop offset="1" stop-color="#6cc3b8" stop-opacity="0.55"/>
        </linearGradient>
      </defs>

      <path class="sea-wave sea-wave--blue" d="M0 190 C200 150 420 180 600 230 L600 470 C420 410 220 420 0 470 Z" fill="url(#wave-blue-band)"/>
      <path class="sea-wave sea-wave--red" d="M380 300 C600 250 820 170 978 160 L978 480 C800 470 600 500 380 470 Z" fill="url(#wave-red-band)"/>

      <g role="img" aria-label="Map of the island in the background">
        <path class="island-map" d="M250 150 C330 110 430 140 520 105 C600 90 660 120 700 160 C770 210 800 300 770 380 C740 460 660 520 560 560 C470 590 410 580 370 520 C330 470 290 440 250 400 C210 350 195 300 215 240 C225 200 230 170 250 150 Z" fill="url(#island-tone)"/>
      </g>

      <g role="img" aria-label="Runners crossing the finish line with arms raised">
        <rect class="runner-picture" x="692" y="62" width="208" height="350" rx="30" fill="url(#runner-tone)"/>
      </g>

      <g role="img" aria-label="Island flag">
        <rect class="island-flag" x="482" y="78" width="56" height="36" fill="#e8b82a"/>
      </g>

      <rect class="certificate__frame" x="30" y="36" width="914" height="616" fill="none" stroke="var(--frame-grey)" stroke-width="1.6"/>
    </svg>

    <h1 class="certificate__text event-name">BLUECREST</h1>
    <p class="certificate__text event-distance">50k</p>
    <h2 class="certificate__text event-subtitle">RUNNING CHALLENGE</h2>

    <p class="certificate__text awarded-label">AWARDED TO:</p>
    <div class="awardee-line"></div>
    <p class="certificate__text awardee-name">Your Name</p>

    <p class="certificate__text award-date">08-22-2019</p>
    <p class="certificate__text award-location">Location: Pier 4, Harbourside</p>
  </main>
</body>
</html>
```